Book Cover Design Project

NOTE. I need the design in four days of posting this!

This will be the cover of my first book, WALK THE HIGH LINE -
alchemy in the real business world. The book explains defines what Purpose and Meaning is, and how to use it in business. I have included the first chapter to provide a background.

I want the core colours to be black and white, and use the colours Violet, Cerulean Blue Extra Pale (powder blue), Cadmium Lemon (flouro yellow). I plan on using this design as the basis for future books in the WALK THE HIGH LINE series, where the yellow is carried through but the violet and blue colours changing.

This is a spiritual business book without using any spiritual language. It is strongly masculine and direct in its nature.

What I am looking for is something Remarkable that captures my reader immediately. My reader is a seeker. He/she is an entrepreneur perhaps looking to setup a new venture and looking for new and better ways of doing things, or he/she may be a small/medium business owner perhaps bored looking for more meaning in personal and business life), or the corporate person who is looking to get out and do something new. Age 35-50.
Updates

Hi I want to correct the paper size. It is "C Format" (trade paperbacks) are 135mm x 216mm (5.32" x 8.51").

Thks

Reason: A deadline has changed which means the completion of this book cover is less time-critical.

This is a business book that introduces new concepts, such as Purpose. Although it is based on spiritual principals  it is using normal business language when explaining what Purpose is, and how businesses can identify it and use it to be more successful.

If there is a border between a self-help and a business book, this book sits close to the border but markedly on the business side.

Hi I want to confirm the book size. The book size I require is the Australian C Format, which measures 153mm W x 234mm H. 

Sorry for any confusion

Reason: Hi I have extended the deadline as I want to be able to print prospective covers and see how they look like in a bookshop next to other covers.

Reason: To allow for final negotiations.

Industry/Entity Type

Business

```html
<!DOCTYPE html>
<html lang="en">
<head>
<meta charset="utf-8">
<title>Walk the High Line – Front Cover</title>
<link rel="stylesheet" href="https://fonts.googleapis.com/css2?family=Questrial&family=Jost:wght@700&family=Source+Sans+3:wght@300&display=swap">
<style>
  :root {
    --paper: #ffffff;
    --ink: #000000;
    --violet: #92278f;
    --lemon: #fff200;
    --author: #ffffff;
  }
  html, body {
    margin: 0;
    padding: 0;
    width: 927px;
    height: 1200px;
    overflow: hidden;
    background: var(--paper);
  }
  .cover-sheet {
    display: block;
    width: 927px;
    height: 1200px;
  }
  .sheet-label {
    font-family: "Source Sans 3", "Myriad Pro", sans-serif;
    font-weight: 300;
    font-size: 26px;
    fill: var(--violet);
  }
  .cover-panel { fill: var(--ink); }
  .cover-arch { fill: var(--violet); }
  .title-walk {
    font-family: "Questrial", "Century Gothic", sans-serif;
    font-size: 170px;
    fill: var(--lemon);
  }
  .title-the {
    font-family: "Questrial", "Century Gothic", sans-serif;
    font-size: 62px;
    fill: var(--violet);
  }
  .title-highline {
    font-family: "Jost", "Futura", sans-serif;
    font-weight: 700;
    font-size: 68px;
    fill: var(--lemon);
  }
  .author-credit {
    font-family: "Source Sans 3", Arial, sans-serif;
    font-weight: 300;
    font-size: 13px;
    fill: var(--author);
  }
</style>
</head>
<body>
<svg class="cover-sheet" viewBox="0 0 600 777" xmlns="http://www.w3.org/2000/svg">
  <text class="sheet-label" x="133" y="80">FRONT COVER</text>

  <path class="cover-panel" d="M113 112 H497 V645 A222.6 222.6 0 0 0 113 645 Z"/>

  <g class="cover-title">
    <text class="title-walk" x="140" y="300" textLength="332" lengthAdjust="spacingAndGlyphs">walk</text>
    <text class="title-the" x="470" y="372" text-anchor="end">the</text>
    <text class="title-highline" x="143" y="437" textLength="327" lengthAdjust="spacingAndGlyphs">HIGH LINE</text>
  </g>

  <text class="author-credit" x="283" y="462">By Anders Halvorsen</text>

  <path class="cover-arch" d="M155 727 A154 154 0 0 1 457 727 H389 A88 88 0 0 0 223 727 Z"/>
</svg>
</body>
</html>
```